Italian Restaurant Responsive Wordpress Website Design

Italian Restaurant is looking to create a new responsive website design based on some Wordpress templates that have been selected as favourites. We want to base the influence of the design off a business card that was recently created (attached below).
The design should be based of these templates that will be purchased when selected. All templates are responsive. Please read details of templates to learn more about their functions and features. After we select the designs we can deliver the customizable PSD files.
http://layoutmarket.example/item/tavola-responsive-restaurant-wordpress-theme/full_screen_preview/7316428
http://pelmodesigns.example/themes/?theme=Caldora
http://themes.brightwexel.example/fettora/
http://www.tablekitlayouts.example/
Pages required
Homepage
-Navigation
-Contact info always accessible on all responsive viewports. You may have to include a design for Contact info on mobile viewport to the top of the page.
-Hours of Operation
About Page
Menu
-Styling of content will be very identical to menu's. That will be provided once I receive a copy.
Gallery
Contact Page
-Show a map, Contact Details and a Contact/Feedback Form
We are open to any designs that you want to lay on top of these Template designs. The current site is: www.quartolume.example If you want an indication of content.
Any questions please ask! Enjoy!
Updates
Hello Everyone. I just updated the menu being used in the restaurant as well as the fonts that are being used as we speak. Any questions please email me. Cheers.
Target Market(s)
The Target Market is families and a more distinguished crowd. They offer valued gourmet food but are located in a very high end neighbourhood. Want to deliver home made cuisine that's approachable but yet considered gourmet.
Industry/Entity Type
Business
Look and feel
Each slider illustrates characteristics of the customer's brand and the style your logo design should communicate.

```html
<!DOCTYPE html>
<html lang="en">
<head>
<meta charset="utf-8">
<title>Quarto Lume — Italian Restaurant</title>
<link href="https://fonts.googleapis.com/css2?family=Roboto+Condensed:wght@400;700&family=PT+Sans:ital,wght@0,400;0,700;1,400&display=swap" rel="stylesheet">
<style>
:root{
  --red:#a8281f;
  --red-dark:#8e1f18;
  --red-tile:#c2453a;
  --charcoal:#262626;
  --charcoal-2:#1b1b1b;
  --header:#2e2e2e;
  --orange:#f0892a;
  --cream:#ebe6dc;
  --cream-2:#ddd6c9;
  --ink:#3a3a3a;
  --white:#ffffff;
}
*{box-sizing:border-box;margin:0;padding:0}
html,body{width:1200px;height:2663px;overflow:hidden}
body{position:relative;background:var(--cream);font-family:"PT Sans",Arial,sans-serif;color:var(--ink)}
.abs{position:absolute}
.photo{display:block}

/* nav */
.topnav{left:0;top:0;width:1200px;height:44px;background:var(--red)}
.topnav ul{list-style:none;position:absolute;left:183px;top:0;width:836px;height:44px;display:flex;justify-content:space-between}
.topnav li{font:700 14px "Roboto Condensed",sans-serif;color:var(--white);text-transform:uppercase;line-height:44px;padding:0 32px}
.topnav li.active{background:var(--charcoal)}

/* header */
.masthead{left:0;top:44px;width:1200px;height:130px;background:var(--header)}
.vip-title{left:181px;top:38px;font:700 15px "Roboto Condensed",sans-serif;color:var(--orange);text-transform:uppercase}
.vip-btn{left:181px;top:66px;width:96px;height:30px;background:var(--orange);color:var(--white);font:700 15px "Roboto Condensed",sans-serif;line-height:30px;text-align:center}
.vip-text{left:286px;top:71px;font:700 15px "Roboto Condensed",sans-serif;color:var(--white);text-transform:uppercase}
.contact-block{left:760px;top:36px}
.contact-block .name{font:700 16px "Roboto Condensed",sans-serif;color:var(--orange);text-transform:uppercase}
.contact-block .addr{font:700 16px "Roboto Condensed",sans-serif;color:var(--white);text-transform:uppercase;margin-top:6px}
.contact-block .call{font:700 16px "Roboto Condensed",sans-serif;color:var(--orange);margin-top:8px}
.social{display:flex;gap:6px;margin-top:8px}
.social span{width:18px;height:18px;border-radius:50%;background:#5a5a5a}
.brand-badge{left:502px;top:52px;width:196px;height:196px;border-radius:50%;background:#3a3a3a;border:6px solid #4a4a4a;display:flex;align-items:center;justify-content:center;z-index:3}
.brand-badge::before{content:"";position:absolute;inset:8px;border:2px dotted #9a9a9a;border-radius:50%}
.brand-badge span{font:700 26px "Roboto Condensed",sans-serif;color:#f1c4bd;text-transform:uppercase}

/* hero */
.hero{left:0;top:174px;width:1200px;height:497px}
.hero-arrow{top:398px;width:42px;height:42px;border-radius:50%;border:2px solid rgba(255,255,255,.7);background:rgba(0,0,0,.25)}

/* feature cards */
.feature{top:600px;width:275px;height:190px;background:var(--white);padding:8px;box-shadow:0 1px 4px rgba(0,0,0,.25)}
.feature h3{height:38px;background:var(--red);color:var(--white);font:700 16px "Roboto Condensed",sans-serif;text-transform:uppercase;text-align:center;line-height:38px}
.feature-text{top:806px;width:266px;font-size:9.5px;line-height:19px;color:#333}
.btn-more{top:907px;width:148px;height:35px;background:var(--red);color:var(--white);font:400 14px "Roboto Condensed",sans-serif;text-align:center;line-height:35px;border:1px solid var(--red-dark);box-shadow:0 1px 2px rgba(0,0,0,.3)}

/* welcome */
.section-title{font:700 28px "Roboto Condensed",sans-serif;color:var(--red);text-transform:uppercase}
.welcome-photo{left:183px;top:1051px;width:311px;height:211px;background:var(--white);padding:6px;box-shadow:0 1px 4px rgba(0,0,0,.25)}
.welcome-copy{left:525px;top:1046px;width:497px;font-size:9.5px;line-height:19px;color:#333}
.welcome-copy p+p{margin-top:9px}
.note{left:525px;top:1216px;width:280px;font-size:9.5px;line-height:22px;font-style:italic;color:#333}
.note b{font:700 14px "Roboto Condensed",sans-serif;color:var(--red);font-style:normal}
.phone-box{left:806px;top:1210px;width:213px;height:52px;background:var(--white);border:2px solid #d9d4ca;display:flex;align-items:center;justify-content:center;gap:8px;font:400 24px "Roboto Condensed",sans-serif;color:var(--red)}

/* events */
.events{left:0;top:1317px;width:1200px;height:449px;background:var(--cream-2)}
.pager{display:flex;gap:3px}
.pager span{width:24px;height:24px;background:#c93a2c;display:flex;align-items:center;justify-content:center}
.event-photo{top:1397px;width:254px;height:147px;background:var(--white);padding:4px;box-shadow:0 1px 3px rgba(0,0,0,.25)}
.event-title{top:1560px;font:700 14px "Roboto Condensed",sans-serif;color:var(--red);text-transform:uppercase}
.event-date{top:1584px;font-size:10px;font-style:italic;color:var(--red)}
.event-rule{height:1px;background:#bdb5a6;width:254px}
.event-text{top:1620px;width:254px;font-size:9.5px;line-height:18px;color:#333}
.event-meta{top:1718px;width:254px;display:flex;align-items:center;font-size:10px;font-style:italic;color:var(--red)}
.stars{display:flex;gap:1px;margin-right:14px}
.comments{display:flex;align-items:center;gap:6px}
.readmore{margin-left:auto}

/* popular */
.popular{left:0;top:1766px;width:1200px;height:581px;background:var(--red)}
.popular-title{left:0;width:1200px;top:28px;text-align:center;font:700 28px "Roboto Condensed",sans-serif;color:var(--white);text-transform:uppercase}
.popular-lead{left:190px;width:820px;top:80px;text-align:center;font-size:11px;line-height:22px;color:var(--white)}
.tile{width:192px;height:188px;background:var(--red-tile);padding:7px;box-shadow:0 1px 3px rgba(0,0,0,.3)}
.tile .photo{width:178px;height:138px}
.tile p{font:700 14px "Roboto Condensed",sans-serif;color:var(--white);text-transform:uppercase;margin-top:11px;padding-left:4px}

/* footer */
.footer{left:0;top:2347px;width:1200px;height:255px;background:var(--charcoal)}
.foot-title{top:32px;font:700 15px "Roboto Condensed",sans-serif;color:var(--white);text-transform:uppercase}
.foot-text{font-size:9px;line-height:14px;color:#9a9a9a}
.hours{top:110px;left:183px;display:grid;grid-template-columns:60px 110px 50px 110px;row-gap:4px;font-size:9.5px;color:var(--white)}
.foot-btn{height:18px;padding:0 12px;background:#4a4a4a;color:#cfcfcf;font-size:8.5px;line-height:18px;text-transform:uppercase}
.tweet-link{color:#e0453a}
.bottom-bar{left:0;top:2602px;width:1200px;height:61px;background:var(--charcoal-2)}
.bottom-links{left:183px;top:23px;font-size:10px;color:#9a9a9a;word-spacing:6px}
.copyright{left:800px;top:23px;font-size:9.5px;color:#9a9a9a}
</style>
</head>
<body>

<nav class="abs topnav">
  <ul>
    <li class="active">Home</li><li>Info</li><li>Menus</li><li>Gallery</li><li>Groups</li><li>VIP List</li><li>Contact</li>
  </ul>
</nav>

<header class="abs masthead">
  <div class="abs vip-title">Join our VIP list</div>
  <div class="abs vip-btn">CLICK HERE</div>
  <div class="abs vip-text">To become a VIP member now.</div>
  <div class="abs contact-block">
    <div class="name">Quarto Lume</div>
    <div class="addr">418 Marlowe Ave. W. Fairhaven, ON</div>
    <div class="call">CALL US : (555) 214-0377</div>
    <div class="social"><span></span><span></span><span></span><span></span><span></span></div>
  </div>
</header>

<div class="abs brand-badge"><span>Quarto Lume</span></div>

<section class="abs hero photo" role="img" aria-label="Close-up of sliced grilled chicken breast with roasted potatoes" style="background:linear-gradient(160deg,#d9a25a 0%,#b8662c 35%,#e2b487 60%,#9e4e22 85%,#6d3216 100%)"></section>
<div class="abs hero-arrow" style="left:90px"></div>
<div class="abs hero-arrow" style="left:1068px"></div>

<article class="abs feature" style="left:186px">
  <h3>Delicious Pancakes</h3>
  <div class="photo" role="img" aria-label="Grilled meat and vegetable skewers" style="height:136px;margin-top:6px;background:linear-gradient(135deg,#d2541b,#8a3a12 60%,#5f7a2a)"></div>
</article>
<article class="abs feature" style="left:470px">
  <h3>Delicious Pancakes</h3>
  <div class="photo" role="img" aria-label="Wraps filled with ham and fresh salad" style="height:136px;margin-top:6px;background:linear-gradient(135deg,#e9d8bf,#c77a62 55%,#7a8d3a)"></div>
</article>
<article class="abs feature" style="left:753px">
  <h3>Delicious Pancakes</h3>
  <div class="photo" role="img" aria-label="Noodle stir fry with greens and red peppers" style="height:136px;margin-top:6px;background:linear-gradient(135deg,#3e6b2a,#b34b2a 55%,#5a3a22)"></div>
</article>

<p class="abs feature-text" style="left:197px">we love to accommodate. We have a wide-ranging drink options with over 65 kinds of wine by bottle or by the glass and amazing beer selections. We want everyone to feel comfortable. We look forward to seeing you!</p>
<p class="abs feature-text" style="left:481px">we love to accommodate. We have a wide-ranging drink options with over 65 kinds of wine by bottle or by the glass and amazing beer selections. We want everyone to feel comfortable. We look forward to seeing you!</p>
<p class="abs feature-text" style="left:764px">we love to accommodate. We have a wide-ranging drink options with over 65 kinds of wine by bottle or by the glass and amazing beer selections. We want everyone to feel comfortable. We look forward to seeing you!</p>

<div class="abs btn-more" style="left:241px">Read More [+]</div>
<div class="abs btn-more" style="left:524px">Read More [+]</div>
<div class="abs btn-more" style="left:807px">Read More [+]</div>

<h2 class="abs section-title" style="left:181px;top:987px">Welcome to Quarto Lume</h2>
<div class="abs welcome-photo">
  <div class="photo" role="img" aria-label="Chef in white hat plating a dessert" style="width:100%;height:100%;background:linear-gradient(135deg,#e8e4df,#c9bfb3 50%,#8a6e58)"></div>
</div>
<div class="abs welcome-copy">
  <p>Located in the heart of Marlowe West, Quarto Lume is named for the most highly - refined italian flour, our key ingredient in our superior pizza and pasta. Valerio's pride &amp; joy: an Italian joint</p>
  <p>showcasing his Barese heritage. Our menu consists mostly of comfort food, offering a restaurant atmosphere for families and making it a tradition. We offer gluten free and whole-wheat options for our Wood Burning pizza and pasta. We cater to everyone, whether your want penne with butter or the kids want a plain cheese pizza, we love to accommodate. We have a wide-ranging drink options with over 65 kinds of wine by bottle or by the glass and amazing beer selections. We want everyone to feel comfortable. We look forward to seeing you!</p>
</div>
<p class="abs note"><b>PLEASE NOTE :</b> Quarto Lume welcomes reservations and encourages walk-ins at anytime. Please call anytime.</p>
<div class="abs phone-box">
  <svg width="24" height="24" viewBox="0 0 24 24"><path d="M6.6 10.8c1.4 2.8 3.8 5.1 6.6 6.6l2.2-2.2c.3-.3.7-.4 1-.2 1.1.4 2.3.6 3.6.6.6 0 1 .4 1 1V20c0 .6-.4 1-1 1C10.6 21 3 13.4 3 4c0-.6.4-1 1-1h3.5c.6 0 1 .4 1 1 0 1.3.2 2.5.6 3.6.1.3 0 .7-.2 1z" fill="#9a9a9a"/></svg>
  (555) 214-0377
</div>

<section class="abs events">
  <h2 class="abs section-title" style="left:0;width:1200px;top:22px;text-align:center">Upcoming Events</h2>
  <div class="abs pager" style="left:966px;top:27px">
    <span><svg width="8" height="10" viewBox="0 0 8 10"><path d="M6 1 2 5l4 4" stroke="#fff" stroke-width="2" fill="none"/></svg></span>
    <span><svg width="8" height="10" viewBox="0 0 8 10"><path d="M2 1l4 4-4 4" stroke="#fff" stroke-width="2" fill="none"/></svg></span>
  </div>
</section>

<div class="abs event-photo" style="left:183px"><div class="photo" role="img" aria-label="Diners sharing a pasta dish at a table" style="width:100%;height:100%;background:linear-gradient(135deg,#7a3a14,#c46a2a 50%,#e0a860)"></div></div>
<div class="abs event-photo" style="left:476px"><div class="photo" role="img" aria-label="Plate of curry with rice and side bowls" style="width:100%;height:100%;background:linear-gradient(135deg,#3a2a1e,#c07a2a 50%,#f1d27a)"></div></div>
<div class="abs event-photo" style="left:769px"><div class="photo" role="img" aria-label="Grilled steak with potatoes and tomatoes" style="width:100%;height:100%;background:linear-gradient(135deg,#e9c65a,#6a2e18 55%,#c23a22)"></div></div>

<h3 class="abs event-title" style="left:183px">Restaurant atmosphere for families</h3>
<h3 class="abs event-title" style="left:476px">Restaurant atmosphere for families</h3>
<h3 class="abs event-title" style="left:769px">Restaurant atmosphere for families</h3>
<div class="abs event-date" style="left:183px">Posted on 27 Oct 2013</div>
<div class="abs event-date" style="left:476px">Posted on 27 Oct 2013</div>
<div class="abs event-date" style="left:769px">Posted on 27 Oct 2013</div>
<div class="abs event-rule" style="left:183px;top:1607px"></div>
<div class="abs event-rule" style="left:476px;top:1607px"></div>
<div class="abs event-rule" style="left:769px;top:1607px"></div>
<p class="abs event-text" style="left:183px">Located in the heart of Marlowe West, Quarto Lume is named for the most highly - refined italian flour, our key ingredient in our superior pizza and pasta. Valerio's pride &amp; joy key ingredient in our superior pizza and pasta...</p>
<p class="abs event-text" style="left:476px">Located in the heart of Marlowe West, Quarto Lume is named for the most highly - refined italian flour, our key ingredient in our superior pizza and pasta. Valerio's pride &amp; joy key ingredient in our superior pizza and pasta...</p>
<p class="abs event-text" style="left:769px">Located in the heart of Marlowe West, Quarto Lume is named for the most highly - refined italian flour, our key ingredient in our superior pizza and pasta. Valerio's pride &amp; joy key ingredient in our superior pizza and pasta...</p>
<div class="abs event-rule" style="left:183px;top:1706px"></div>
<div class="abs event-rule" style="left:476px;top:1706px"></div>
<div class="abs event-rule" style="left:769px;top:1706px"></div>

<div class="abs event-meta" style="left:183px">
  <svg class="stars" width="76" height="13" viewBox="0 0 76 13"><g fill="#e6a13a"><path id="st" d="M6.5 0l2 4.2 4.5.6-3.3 3.1.8 4.6-4-2.2-4 2.2.8-4.6L0 4.8l4.5-.6z"/><use href="#st" x="15"/><use href="#st" x="30"/></g><g fill="#9a9a9a"><use href="#st" x="45"/><use href="#st" x="60"/></g></svg>
  <span class="comments"><svg width="11" height="10" viewBox="0 0 11 10"><path d="M0 0h11v7H4L1 10V7H0z" fill="#a8281f"/></svg>102 comments</span>
  <span class="readmore">[ Readmore ]</span>
</div>
<div class="abs event-meta" style="left:476px">
  <svg class="stars" width="76" height="13" viewBox="0 0 76 13"><g fill="#e6a13a"><use href="#st"/><use href="#st" x="15"/><use href="#st" x="30"/></g><g fill="#9a9a9a"><use href="#st" x="45"/><use href="#st" x="60"/></g></svg>
  <span class="comments"><svg width="11" height="10" viewBox="0 0 11 10"><path d="M0 0h11v7H4L1 10V7H0z" fill="#a8281f"/></svg>102 comments</span>
  <span class="readmore">[ Readmore ]</span>
</div>
<div class="abs event-meta" style="left:769px">
  <svg class="stars" width="76" height="13" viewBox="0 0 76 13"><g fill="#e6a13a"><use href="#st"/><use href="#st" x="15"/><use href="#st" x="30"/></g><g fill="#9a9a9a"><use href="#st" x="45"/><use href="#st" x="60"/></g></svg>
  <span class="comments"><svg width="11" height="10" viewBox="0 0 11 10"><path d="M0 0h11v7H4L1 10V7H0z" fill="#a8281f"/></svg>102 comments</span>
  <span class="readmore">[ Readmore ]</span>
</div>

<section class="abs popular">
  <h2 class="abs popular-title">Most Popular</h2>
  <div class="abs pager" style="left:954px;top:30px">
    <span style="background:var(--red-dark)"><svg width="8" height="10" viewBox="0 0 8 10"><path d="M6 1 2 5l4 4" stroke="#fff" stroke-width="2" fill="none"/></svg></span>
    <span style="background:var(--red-dark)"><svg width="8" height="10" viewBox="0 0 8 10"><path d="M2 1l4 4-4 4" stroke="#fff" stroke-width="2" fill="none"/></svg></span>
  </div>
  <p class="abs popular-lead">Many desktop publishing packages and web page editors now use Lorem Ipsum as their default model text, and a search for 'lorem ipsum' will uncover many web sites still in their infancy. Various versions have evolved over the years, sometimes by accident, sometimes on purpose</p>

  <div class="abs tile" style="left:181px;top:142px"><div class="photo" role="img" aria-label="Sliced steak with greens" style="background:linear-gradient(135deg,#f2eeea,#7a2e1c 55%,#3a5a22)"></div><p>Insalata della casa</p></div>
  <div class="abs tile" style="left:394px;top:142px"><div class="photo" role="img" aria-label="Nachos with salsa and guacamole" style="background:linear-gradient(135deg,#d8b04a,#b8321e 50%,#6a8a2a)"></div><p>Insalata della casa</p></div>
  <div class="abs tile" style="left:609px;top:142px"><div class="photo" role="img" aria-label="Creamy pasta in a white bowl" style="background:linear-gradient(135deg,#f4efe6,#e2b670 55%,#b5642a)"></div><p>Insalata della casa</p></div>
  <div class="abs tile" style="left:824px;top:142px"><div class="photo" role="img" aria-label="Steak with broccoli" style="background:linear-gradient(135deg,#2e5a1e,#5a2a16 55%,#e9e6e0)"></div><p>Insalata della casa</p></div>

  <div class="abs tile" style="left:181px;top:357px"><div class="photo" role="img" aria-label="Stacked burger with lettuce and cheese" style="background:linear-gradient(180deg,#d99a3a,#5a2e16 45%,#4a8a2a 65%,#c98a3a)"></div><p>Insalata della casa</p></div>
  <div class="abs tile" style="left:394px;top:357px"><div class="photo" role="img" aria-label="Fried croquettes in a bowl" style="background:linear-gradient(135deg,#6a3a1a,#c07a2a 50%,#8a4a1a)"></div><p>Insalata della casa</p></div>
  <div class="abs tile" style="left:609px;top:357px"><div class="photo" role="img" aria-label="Glazed duck breast with salad" style="background:linear-gradient(135deg,#e9e2d6,#9a4a22 50%,#5a7a2a)"></div><p>Insalata della casa</p></div>
  <div class="abs tile" style="left:824px;top:357px"><div class="photo" role="img" aria-label="Flatbread with dips and salad" style="background:linear-gradient(135deg,#f4f1ec,#d9b27a 55%,#6a8a3a)"></div><p>Insalata della casa</p></div>
</section>

<footer class="abs footer">
  <h4 class="abs foot-title" style="left:183px">Operating Hours</h4>
  <p class="abs foot-text" style="left:183px;top:66px;width:320px">Hours may change during holidays or special occasions. Always contact Quarto Lume for specific information.</p>
  <div class="abs hours">
    <span>Monday</span><span>: 11:00am-10:00pm</span><span>Friday</span><span>: 11:00am-10:00pm</span>
    <span>Tuesday</span><span>: 11:00am-10:00pm</span><span>Saturday</span><span>: 11:00am-10:00pm</span>
    <span>Wednesday</span><span>: 11:00am-11:00pm</span><span>Sunday</span><span>: 11:00am-11:00pm</span>
    <span>Thursday</span><span>: 11:00am-11:00pm</span><span></span><span></span>
  </div>
  <div class="abs foot-btn" style="left:184px;top:210px">Daily Specials</div>

  <h4 class="abs foot-title" style="left:535px;top:28px">About Us</h4>
  <div class="abs foot-text" style="left:535px;top:60px;width:224px">
    <p>Located in the heart of Marlowe West, Quarto Lume is named for the most highly - refined italian flour, our key ingredient in our superior pizza and pasta. Valerio's pride &amp; joy: an Italian joint</p>
    <p style="margin-top:8px">showcasing his Barese heritage. Our menu consists mostly of comfort food, offering a restaurant atmosphere for families and making it a tradition. We offer gluten free options...</p>
  </div>
  <div class="abs foot-btn" style="left:701px;top:210px">View More</div>

  <h4 class="abs foot-title" style="left:800px;top:28px;display:flex;align-items:center;gap:8px"><span style="width:12px;height:12px;border-radius:50%;background:#5a5a5a"></span>Latest Tweets</h4>
  <div class="abs foot-text" style="left:800px;top:60px;width:222px">
    <p>Be sure to check out the insane comedy stage magic of one of East Coast's Top Rated premiere entertainers...</p>
    <p class="tweet-link">http://www.quartolume.example/</p>
    <p style="margin-top:20px">Be sure to check out the insane comedy stage magic of one of East Coast's Top Rated premiere entertainers...</p>
    <p class="tweet-link">http://www.quartolume.example/</p>
  </div>
  <div class="abs foot-btn" style="left:956px;top:210px">View More</div>
</footer>

<div class="abs bottom-bar">
  <div class="abs bottom-links">Home | Info | Menus | Gallery | Groups | VIP List | Contact</div>
  <div class="abs copyright">Copyright © 2013 Quarto Lume. All rights reserved.</div>
</div>

</body>
</html>
```